Dellwick Underwriters LLC product offerings and how to contact for quotes

A marketing email to new and current clients explaining the products the MGA offers and it's exclusive programs. Looking for a modern/sleek design that catches the eye and doesn't become the traditional spam email. Needs to have hyper links to website.
You can use the current website for details of product offerings for insurance: www.dellwick-uw.example.
Target Market(s)
Long haul trucking
Industry/Entity Type
Trucking
Colors
0054AA
0677BA
7BADD7
CADEEF
E8F1F8
Requirements
Must have
- Color theme, informative, use of trucking art. Links to website.
Nice to have
- Catchy subject line; want to catch readers eye

```html
<!DOCTYPE html>
<html lang="en">
<head>
<meta charset="utf-8">
<title>Dellwick Underwriters – Products &amp; Programs</title>
<link href="https://fonts.googleapis.com/css2?family=Poppins:wght@400;500;600;700;800&display=swap" rel="stylesheet">
<style>
:root{
  --blue-deep:#0054AA;
  --blue-mid:#0677BA;
  --blue-soft:#7BADD7;
  --blue-pale:#CADEEF;
  --blue-mist:#E8F1F8;
  --card-bg:#EEF3F9;
  --ink:#2b2b2b;
  --white:#ffffff;
}
*{margin:0;padding:0;box-sizing:border-box}
html,body{width:1200px;height:3393px;overflow:hidden;background:var(--white);font-family:'Poppins',sans-serif;color:var(--ink)}
.page{position:relative;width:1200px;height:3393px}

/* header */
.header{position:absolute;left:0;top:0;width:1200px;height:165px;background:var(--white)}
.header-panel{position:absolute;left:0;top:0}
.brand{position:absolute;display:flex;align-items:center;gap:14px;color:var(--blue-deep);font-weight:700;letter-spacing:.5px}
.brand-top{left:112px;top:50px;font-size:46px}
.brand-dot{width:22px;height:22px;background:var(--blue-mid)}
.expert{position:absolute;left:778px;top:38px;color:var(--white)}
.expert-label{font-size:19px;font-weight:500;letter-spacing:.3px}
.expert-phone{font-size:40px;font-weight:700;line-height:1.2;letter-spacing:1px;color:var(--white);text-decoration:none}
.phone-badge{position:absolute;left:667px;top:38px;width:87px;height:87px;border-radius:50%;background:var(--white);display:flex;align-items:center;justify-content:center}

/* hero */
.hero{position:absolute;left:0;top:165px;width:1200px;height:650px}
.hero-title{position:absolute;left:112px;top:110px;color:var(--white);font-size:51px;font-weight:800;line-height:60px;width:620px}

/* section titles */
.section-title{text-align:center;font-weight:800;font-size:54px;line-height:60px}
.divider{display:flex;align-items:center;justify-content:center;gap:10px;margin-top:10px}
.divider span{display:block;width:98px;height:2px}
.divider i{display:block;width:12px;height:12px;border-radius:50%}

.products{position:absolute;left:0;top:848px;width:1200px}
.products .section-title{color:var(--blue-deep)}
.products .divider span,.products .divider i{background:var(--blue-mid)}

.grid{position:absolute;left:112px;top:140px;display:grid;grid-template-columns:repeat(3,300px);column-gap:37.5px;row-gap:36px}
.card{background:var(--card-bg);position:relative;height:545px}
.card.row2{height:515px}
.card-photo{height:204px;width:300px;display:block}
.card-badge{position:absolute;left:102px;top:117px;width:96px;height:108px}
.card-title{margin-top:56px;text-align:center;color:var(--blue-deep);font-weight:600;font-size:22.5px;line-height:30px;padding:0 30px}
.card-text{margin-top:14px;text-align:center;font-size:16.5px;line-height:28.5px;padding:0 22px;color:var(--ink)}

/* programs */
.programs{position:absolute;left:0;top:2190px;width:1200px;height:780px;background:linear-gradient(100deg,#0b57ad 0%,#0a6dc0 55%,#1a9ad8 100%);color:var(--white)}
.programs .section-title{margin-top:102px;color:var(--white)}
.programs .divider span,.programs .divider i{background:var(--white)}
.programs-copy{width:960px;margin:24px auto 0;text-align:center;font-size:28px;line-height:43.5px;font-weight:500}
.cta{display:block;width:247px;height:83px;margin:45px auto 0;border-radius:42px;background:var(--white);color:#1d1d2b;font-weight:700;font-size:24px;line-height:83px;text-align:center;text-decoration:none;letter-spacing:.5px}

/* footer */
.footer{position:absolute;left:0;top:2970px;width:1200px;height:423px;background:var(--blue-mist)}
.brand-foot{left:50%;transform:translateX(-50%);top:80px;font-size:50px}
.footer-contact{position:absolute;top:225px;width:100%;text-align:center;font-size:24px;color:#1e1e1e}
.footer-contact .sep{margin:0 14px}
.footer-link{position:absolute;top:270px;width:100%;text-align:center}
.footer-link a{font-size:30px;font-weight:500;color:var(--blue-mid);text-decoration:none;border-bottom:2px solid var(--blue-mid)}
.footer-rule{position:absolute;left:112px;top:340px;width:975px;height:1px;background:#cfd6de}
.copyright{position:absolute;top:366px;width:100%;text-align:center;font-size:21px;color:#333}
</style>
</head>
<body>
<div class="page">

  <header class="header">
    <svg class="header-panel" width="1200" height="165" viewBox="0 0 1200 165" aria-hidden="true">
      <defs>
        <linearGradient id="panelGrad" x1="0" y1="0" x2="1" y2="0">
          <stop offset="0" stop-color="#0054AA"/>
          <stop offset="1" stop-color="#1a9ad8"/>
        </linearGradient>
      </defs>
      <polygon points="675,0 1200,0 1200,165 525,165" fill="url(#panelGrad)"/>
    </svg>
    <div class="brand brand-top"><span class="brand-dot"></span>DELLWICK</div>
    <div class="phone-badge">
      <svg width="44" height="44" viewBox="0 0 24 24" aria-hidden="true">
        <path d="M6.6 10.8a15.1 15.1 0 0 0 6.6 6.6l2.2-2.2c.3-.3.7-.4 1-.2 1.1.4 2.3.6 3.6.6.6 0 1 .4 1 1V20c0 .6-.4 1-1 1A17 17 0 0 1 3 4c0-.6.4-1 1-1h3.5c.6 0 1 .4 1 1 0 1.3.2 2.5.6 3.6.1.3 0 .7-.2 1z" fill="none" stroke="#0054AA" stroke-width="1.8" stroke-linejoin="round"/>
        <path d="M14.5 3.5a6.5 6.5 0 0 1 6 6M14.5 6.8a3.3 3.3 0 0 1 2.8 2.8" fill="none" stroke="#0054AA" stroke-width="1.8" stroke-linecap="round"/>
      </svg>
    </div>
    <div class="expert">
      <div class="expert-label">SPEAK WITH AN EXPERT:</div>
      <a class="expert-phone" href="tel:5550142870">(555)014-2870</a>
    </div>
  </header>

  <section class="hero">
    <svg width="1200" height="650" viewBox="0 0 1200 650" role="img" aria-label="Red semi truck with white trailer driving on a highway through autumn forest">
      <defs>
        <linearGradient id="heroGrad" x1="0" y1="0" x2="1" y2="1">
          <stop offset="0" stop-color="#5a4a2c"/>
          <stop offset=".4" stop-color="#b98a2c"/>
          <stop offset=".7" stop-color="#8a7456"/>
          <stop offset="1" stop-color="#7e8790"/>
        </linearGradient>
      </defs>
      <polygon points="0,0 1200,0 1200,540 975,638 0,470" fill="url(#heroGrad)"/>
      <polygon points="0,0 1200,0 1200,540 975,638 0,470" fill="#1a2430" opacity=".28"/>
      <polygon points="22,428 975,612 960,640 22,452" fill="#0054AA"/>
      <polygon points="990,560 1155,455 1150,495 985,590" fill="#1a9ad8"/>
    </svg>
    <h1 class="hero-title">Specializing in Tough-to-Place Risks with Unmatched Customer Service</h1>
  </section>

  <section class="products">
    <h2 class="section-title">Our Products</h2>
    <div class="divider"><span></span><i></i><span></span></div>

    <div class="grid">
      <article class="card">
        <svg class="card-photo" viewBox="0 0 300 204" role="img" aria-label="White semi trucks parked at a loading dock"><rect width="300" height="204" fill="#8f9aa6"/><rect y="120" width="300" height="84" fill="#c9ced4"/></svg>
        <svg class="card-badge" viewBox="0 0 96 108" aria-hidden="true"><polygon points="48,0 96,27 96,81 48,108 0,81 0,27" fill="#0054AA"/><rect x="24" y="40" width="30" height="22" fill="#fff"/><path d="M56 46h9l7 8v8H56z" fill="#fff"/><circle cx="33" cy="66" r="4" fill="#fff"/><circle cx="63" cy="66" r="4" fill="#fff"/></svg>
        <h3 class="card-title">Auto Liability</h3>
        <p class="card-text">Liability insurance is a part of the general insurance system of risk financing to protect the purchaser (the "insured") from the risks of liabilities imposed by lawsuits and similar claims.</p>
      </article>

      <article class="card">
        <svg class="card-photo" viewBox="0 0 300 204" role="img" aria-label="Two workers reviewing paperwork beside a trailer"><rect width="300" height="204" fill="#9a9488"/><rect x="170" width="130" height="204" fill="#c5c7c9"/></svg>
        <svg class="card-badge" viewBox="0 0 96 108" aria-hidden="true"><polygon points="48,0 96,27 96,81 48,108 0,81 0,27" fill="#0054AA"/><rect x="22" y="44" width="28" height="20" fill="#fff"/><path d="M52 50h8l6 7v7H52z" fill="#fff"/><circle cx="31" cy="67" r="4" fill="#fff"/><circle cx="58" cy="67" r="4" fill="#fff"/><path d="M62 28l10 4v7c0 6-4 10-10 12-6-2-10-6-10-12v-7z" fill="#fff"/><path d="M57 38l4 4 6-7" fill="none" stroke="#0054AA" stroke-width="2.4"/></svg>
        <h3 class="card-title">Non-Trucking Liability</h3>
        <p class="card-text">Non-Trucking Liability (NTL) provides coverage in case you cause an accident while you are using your vehicle for non-business or personal use other than transporting goods or merchandise.</p>
      </article>

      <article class="card">
        <svg class="card-photo" viewBox="0 0 300 204" role="img" aria-label="Tanker truck on a desert highway"><rect width="300" height="204" fill="#a7bfd8"/><rect y="110" width="300" height="94" fill="#8d8a86"/></svg>
        <svg class="card-badge" viewBox="0 0 96 108" aria-hidden="true"><polygon points="48,0 96,27 96,81 48,108 0,81 0,27" fill="#0054AA"/><rect x="24" y="52" width="22" height="16" rx="3" fill="#fff"/><rect x="50" y="52" width="22" height="16" rx="3" fill="#fff"/><path d="M48 24l8 3v6c0 5-3 8-8 10-5-2-8-5-8-10v-6z" fill="#fff"/></svg>
        <h3 class="card-title">Auto Physical Damage</h3>
        <p class="card-text">Physical Damage insurance is a type of insurance that covers damages to your truck and trailer. This type of coverage is typically offered as part of an auto insurance policy.</p>
      </article>

      <article class="card row2">
        <svg class="card-photo" viewBox="0 0 300 204" role="img" aria-label="Cargo being loaded into a box truck"><rect width="300" height="204" fill="#6e5a44"/><rect x="130" width="170" height="204" fill="#d6d6d4"/></svg>
        <svg class="card-badge" viewBox="0 0 96 108" aria-hidden="true"><polygon points="48,0 96,27 96,81 48,108 0,81 0,27" fill="#0054AA"/><rect x="24" y="40" width="30" height="22" fill="#fff"/><path d="M56 46h9l7 8v8H56z" fill="#fff"/><circle cx="33" cy="66" r="4" fill="#fff"/><circle cx="63" cy="66" r="4" fill="#fff"/></svg>
        <h3 class="card-title">Motor Truck Cargo</h3>
        <p class="card-text">Provides liability insurance for truckers who carry the cargo of others and is used in the event that the cargo is destroyed, damaged, stolen, or otherwise declared a loss while in the process</p>
      </article>

      <article class="card row2">
        <svg class="card-photo" viewBox="0 0 300 204" role="img" aria-label="Two semi trucks on a tree-lined road"><rect width="300" height="204" fill="#5f7a54"/><rect y="120" width="300" height="84" fill="#8a8f94"/></svg>
        <svg class="card-badge" viewBox="0 0 96 108" aria-hidden="true"><polygon points="48,0 96,27 96,81 48,108 0,81 0,27" fill="#0054AA"/><path d="M48 24l16 6v14c0 11-7 18-16 22-9-4-16-11-16-22V30z" fill="#fff"/><path d="M41 46l6 6 9-11" fill="none" stroke="#0054AA" stroke-width="3"/><path d="M24 70c8 8 16 10 24 10s16-2 24-10" fill="none" stroke="#fff" stroke-width="4" stroke-linecap="round"/></svg>
        <h3 class="card-title">General Liability</h3>
        <p class="card-text">General liability is often thought of when it comes to situations like a slip and fall. However, not many people realize that it would also cover any damages or bodily injury that your business</p>
      </article>

      <article class="card row2">
        <svg class="card-photo" viewBox="0 0 300 204" role="img" aria-label="Row of parked semi truck cabs"><rect width="300" height="204" fill="#b6c4d2"/><rect y="110" width="300" height="94" fill="#8e9196"/></svg>
        <svg class="card-badge" viewBox="0 0 96 108" aria-hidden="true"><polygon points="48,0 96,27 96,81 48,108 0,81 0,27" fill="#0054AA"/><rect x="24" y="52" width="22" height="16" rx="3" fill="#fff"/><rect x="50" y="52" width="22" height="16" rx="3" fill="#fff"/><path d="M48 24l8 3v6c0 5-3 8-8 10-5-2-8-5-8-10v-6z" fill="#fff"/></svg>
        <h3 class="card-title">Umbrella &amp; Excess Coverage</h3>
        <p class="card-text">Most Umbrella and Excess Liability policies are not written on standardized forms, so it is always important to read your policies to see what they actually cover.</p>
      </article>
    </div>
  </section>

  <section class="programs">
    <h2 class="section-title">MGA Offers &amp;<br>Exclusive Programs</h2>
    <div class="divider"><span></span><i></i><span></span></div>
    <p class="programs-copy">Lorem ipsum dolor sit amet, consectetur adipiscing elit, sed do eiusmod tempor incididunt ut labore et dolore magna aliqua. Ut enim ad minim veniam, quis nostrud exercitation ullamco laboris nisi ut aliquip ex ea commodo consequat. Duis aute irure dolor in reprehenderit in voluptate velit esse cillum dolore eu fugiat nulla pariatur. Excepteur sint occaecatea.</p>
    <a class="cta" href="https://www.dellwick-uw.example">GET STARTED</a>
  </section>

  <footer class="footer">
    <div class="brand brand-foot"><span class="brand-dot"></span>DELLWICK</div>
    <p class="footer-contact">410 Meridian Loop Ste 220 Portland, OR 97201<span class="sep">/</span>(555)014-2870</p>
    <p class="footer-link"><a href="https://www.dellwick-uw.example">www.dellwick-uw.example</a></p>
    <div class="footer-rule"></div>
    <p class="copyright">Copyright © 2025 Dellwick Underwriters LLC</p>
  </footer>

</div>
</body>
</html>
```